Business Card Design for Corvella

Need a business card designed for Corvella employees.
- 2 sided business card
- Front:
Company Logo (file attached)
Background could be:white with perhaps a red/black stripe on the left
OR
Background could be: OR dark red-black gradient: be creative
Include the following on the front:
Marcus Dellow
Founder & CEO
marcus.dellow@corvella-example.com
+1 555.010.0147
corvella-example.com
- Back: White color background with company logo
Text under the logo: Invoice Automation 2.0
** be creative about the font, mix of upper and lower case and colors for the text **
Target Market(s)
We are a software company marketing our products to large and medium sized businesses.
Industry/Entity Type
Business

```html
<!DOCTYPE html>
<html lang="en">
<head>
<meta charset="utf-8">
<title>Corvella Business Card</title>
<link rel="stylesheet" href="https://fonts.googleapis.com/css2?family=Quicksand:wght@400;500;700&display=swap">
<style>
  :root {
    --stage: #2b2b2b;
    --card: #ffffff;
    --brand-red: #9a0b0c;
    --brand-red-deep: #7e0708;
    --brand-red-soft: #b3171a;
    --ink: #1f1f1f;
    --ink-soft: #3a3a3a;
    --ink-muted: #6a6a6a;
    --ghost: #f1f1f1;
  }
  * { box-sizing: border-box; margin: 0; padding: 0; }
  html, body {
    width: 1200px;
    height: 900px;
    overflow: hidden;
    background: var(--stage);
    font-family: "Quicksand", "Helvetica Neue", Arial, sans-serif;
  }
  .stage {
    position: relative;
    width: 1200px;
    height: 900px;
  }
  .card {
    position: absolute;
    top: 203px;
    width: 266px;
    height: 467px;
    background: var(--card);
    box-shadow: 0 4px 14px rgba(0, 0, 0, 0.45);
    overflow: hidden;
  }
  .card--front { left: 338px; }
  .card--back { left: 632px; }

  /* Logo side */
  .front-band {
    position: absolute;
    left: 0;
    top: 0;
    width: 100%;
    height: 286px;
    background: var(--brand-red);
  }
  .front-band__graphic {
    position: absolute;
    left: 0;
    top: 0;
    width: 100%;
    height: 100%;
  }
  .front-band__url {
    position: absolute;
    right: 2px;
    bottom: 0;
    color: #ffffff;
    font-weight: 700;
    font-size: 14px;
    line-height: 1.1;
    letter-spacing: -0.1px;
  }
  .front-wordmark {
    position: absolute;
    left: 0;
    right: 0;
    top: 381px;
    display: flex;
    align-items: center;
    justify-content: center;
    gap: 8px;
  }
  .front-wordmark__dot {
    width: 22px;
    height: 22px;
    border-radius: 50%;
    background: var(--brand-red);
  }
  .front-wordmark__name {
    font-size: 25px;
    font-weight: 500;
    letter-spacing: 1.5px;
    color: var(--ink-soft);
    line-height: 1;
  }
  .front-tagline {
    position: absolute;
    left: 0;
    right: 0;
    top: 418px;
    text-align: center;
    font-size: 11px;
    font-weight: 500;
    letter-spacing: 0.6px;
    color: var(--ink-muted);
  }
  .front-tagline__version {
    color: var(--brand-red);
    font-weight: 700;
  }

  /* Contact side */
  .back-graphic {
    position: absolute;
    left: 0;
    top: 0;
    width: 100%;
    height: 250px;
  }
  .contact {
    position: absolute;
    right: 23px;
    top: 364px;
    text-align: right;
    color: var(--ink);
    line-height: 1.12;
  }
  .contact__name-row {
    display: flex;
    align-items: center;
    justify-content: flex-end;
    gap: 5px;
  }
  .contact__dot {
    width: 12px;
    height: 12px;
    border-radius: 50%;
    background: var(--brand-red);
  }
  .contact__name {
    font-size: 20px;
    font-weight: 700;
    letter-spacing: -0.2px;
  }
  .contact__title,
  .contact__email {
    font-size: 12.5px;
    font-weight: 500;
  }
  .contact__phone {
    margin-top: 6px;
    font-size: 13px;
    font-weight: 500;
  }
</style>
</head>
<body>
  <main class="stage">
    <section class="card card--front" aria-label="Card logo side">
      <div class="front-band">
        <svg class="front-band__graphic" viewBox="0 0 266 286" role="img" aria-label="Large decorative brand symbol in red tones" preserveAspectRatio="none">
          <defs>
            <radialGradient id="frontGlow" cx="0.55" cy="0.4" r="0.6">
              <stop offset="0" stop-color="#b3171a"/>
              <stop offset="0.7" stop-color="#9a0b0c"/>
              <stop offset="1" stop-color="#7e0708"/>
            </radialGradient>
          </defs>
          <rect width="266" height="286" fill="url(#frontGlow)"/>
        </svg>
        <span class="front-band__url">corvella-example.com</span>
      </div>
      <div class="front-wordmark">
        <span class="front-wordmark__dot"></span>
        <span class="front-wordmark__name">Corvella</span>
      </div>
      <p class="front-tagline">Invoice Automation <span class="front-tagline__version">2.0</span></p>
    </section>

    <section class="card card--back" aria-label="Card contact side">
      <svg class="back-graphic" viewBox="0 0 266 250" role="img" aria-label="Faint decorative brand symbol in light grey" preserveAspectRatio="none">
        <defs>
          <radialGradient id="backGlow" cx="0.4" cy="0.4" r="0.55">
            <stop offset="0" stop-color="#f1f1f1"/>
            <stop offset="1" stop-color="#ffffff"/>
          </radialGradient>
        </defs>
        <rect width="266" height="250" fill="url(#backGlow)"/>
      </svg>
      <div class="contact">
        <div class="contact__name-row">
          <span class="contact__dot"></span>
          <span class="contact__name">Marcus Dellow</span>
        </div>
        <div class="contact__title">founder &amp; CEO</div>
        <div class="contact__email">marcus.dellow@corvella-example.com</div>
        <div class="contact__phone">+1 555.010.0147</div>
      </div>
    </section>
  </main>
</body>
</html>
```